Postcard Design for Marketing to Builders

I am an architect that gets most of my work from contractor's. I design residential and commercial projects based in California. My main focus is California's Central Coast. I want the feel of the postcard to reflect a strong professional, efficient and creative partner for contractors (Builders). I have provide some photos of projects I have done recently to use on the postcard if needed. I have also included my logo which I would like on the front.

Industry/Entity Type

Architect

Font styles to use
Serif

```html
<!DOCTYPE html>
<html lang="en">
<head>
<meta charset="utf-8">
<title>Daniel R Harlow Architect – Postcard</title>
<link rel="stylesheet" href="https://fonts.googleapis.com/css2?family=EB+Garamond:wght@400;500&family=Jost:wght@400&display=swap">
<style>
  :root{
    --ink:#2b2a8e;
    --brand-blue:#3a3fa6;
    --brand-orange:#ee6a22;
    --rule:#9fa3cf;
    --frame:#8a8a8a;
    --paper:#ffffff;
    --label:#111111;
  }
  *{box-sizing:border-box;margin:0;padding:0}
  html,body{width:1200px;height:1200px;overflow:hidden;background:var(--paper)}
  body{position:relative;font-family:"EB Garamond",Georgia,serif;color:var(--ink)}
  .side-label{position:absolute;font-family:"Jost",Arial,sans-serif;font-size:18px;letter-spacing:3px;color:var(--label)}
  .side-label--front{left:118px;top:122px}
  .side-label--back{left:126px;top:712px}

  .card{position:absolute;background:var(--paper);border:1px solid #444;overflow:hidden}
  .card--front{left:256px;top:16px;width:890px;height:577px}
  .card--back{left:254px;top:606px;width:892px;height:577px}

  .hero{position:absolute;left:0;top:0;width:888px;height:524px;
    background:
      linear-gradient(180deg,rgba(70,90,50,0) 0%,rgba(70,90,50,0) 68%,rgba(74,86,52,.92) 100%),
      linear-gradient(180deg,rgba(255,255,255,0) 0%,rgba(255,255,255,0) 14%,rgba(0,0,0,0) 100%),
      linear-gradient(100deg,#2a9ce2 0%,#3ba4e6 32%,#86b3cf 44%,#c9b68c 56%,#cdb98e 72%,#b9a87c 86%,#8fa36f 100%);}
  .hero-frame{position:absolute;left:16px;top:17px;width:856px;height:440px;border:1px solid rgba(255,255,255,.8);z-index:1}

  .photo{position:absolute;z-index:2}
  .thumb-1{left:15px;top:436px;width:152px;height:118px;background:linear-gradient(160deg,#8fb07a,#5d6e45)}
  .thumb-2{left:177px;top:436px;width:153px;height:118px;background:linear-gradient(160deg,#b9c6cf,#7d8a86)}
  .thumb-3{left:560px;top:436px;width:152px;height:118px;background:linear-gradient(170deg,#7fb0e0 0%,#c7b49b 45%,#a59378 100%)}
  .thumb-4{left:722px;top:436px;width:152px;height:118px;background:linear-gradient(170deg,#6aa6e6 0%,#c6784a 45%,#8a5a3a 100%)}

  .brand{position:absolute;z-index:2;display:flex;flex-direction:column;align-items:center;justify-content:flex-end;background:var(--paper);padding-bottom:10px}
  .brand--front{left:341px;top:436px;width:208px;height:134px}
  .brand-mark{width:24px;height:24px;background:var(--brand-orange);margin-bottom:14px}
  .brand-name{font-weight:500;color:var(--brand-blue);font-size:19px;letter-spacing:.3px;line-height:1;white-space:nowrap}
  .brand-sub{font-weight:500;color:var(--brand-blue);font-size:8px;letter-spacing:5px;margin-top:3px;border-top:1px solid var(--brand-blue);padding-top:2px;white-space:nowrap}
  .brand--back{left:220px;top:14px;width:156px;height:112px;padding-bottom:14px}
  .brand--back .brand-mark{width:20px;height:20px;margin-bottom:12px}
  .brand--back .brand-name{font-size:14.5px;letter-spacing:.2px}
  .brand--back .brand-sub{font-size:6.5px;letter-spacing:4px}

  .back-photo-1{left:14px;top:14px;width:196px;height:98px;background:linear-gradient(170deg,#5d7d4f 0%,#a8683a 45%,#4e3a2c 100%)}
  .back-photo-2{left:385px;top:14px;width:195px;height:98px;background:linear-gradient(180deg,#4f8fd6 0%,#c9c3ae 50%,#8b8b84 100%)}

  .double-rule{position:absolute;top:127px;height:4px;border-top:1px solid var(--rule);border-bottom:1px solid var(--rule)}
  .double-rule--left{left:14px;width:197px}
  .double-rule--right{left:383px;width:197px}

  .message{position:absolute;left:57px;top:143px;width:520px;font-size:17.8px;line-height:20.8px}
  .message p{margin-bottom:12.6px}
  .message span{display:block;white-space:nowrap}

  .contact{position:absolute;left:14px;top:479px;width:566px;display:flex;align-items:center;gap:12px;font-size:15.4px;letter-spacing:1.5px;white-space:nowrap}
  .contact .line{flex:1;height:1px;background:var(--rule)}

  .divider{position:absolute;left:592px;top:55px;width:1px;height:444px;background:#c8c8c8}
  .stamp-box{position:absolute;left:748px;top:15px;width:127px;height:126px;border:1px solid #bdbdbd}
  .address-line{position:absolute;left:611px;width:264px;height:1px;background:var(--frame)}
</style>
</head>
<body>
  <div class="side-label side-label--front">FRONT</div>
  <div class="side-label side-label--back">BACK</div>

  <section class="card card--front">
    <div class="hero" role="img" aria-label="Three-storey commercial office building fading into a blue blueprint line drawing, with landscaping in front"></div>
    <div class="hero-frame"></div>
    <div class="photo thumb-1" role="img" aria-label="Green two-storey house with porch among trees"></div>
    <div class="photo thumb-2" role="img" aria-label="Light grey house with exterior stair and balcony"></div>
    <div class="brand brand--front">
      <div class="brand-mark"></div>
      <div class="brand-name">DANIEL R HARLOW</div>
      <div class="brand-sub">ARCHITECT</div>
    </div>
    <div class="photo thumb-3" role="img" aria-label="Two-storey stucco house with tile roof and garages"></div>
    <div class="photo thumb-4" role="img" aria-label="Wood-sided building with stone chimney and red roof"></div>
  </section>

  <section class="card card--back">
    <div class="photo back-photo-1" role="img" aria-label="Timber-framed entry porch of a lodge-style building"></div>
    <div class="brand brand--back">
      <div class="brand-mark"></div>
      <div class="brand-name">DANIEL R HARLOW</div>
      <div class="brand-sub">ARCHITECT</div>
    </div>
    <div class="photo back-photo-2" role="img" aria-label="Single-storey building with cupola and parking lot"></div>
    <div class="double-rule double-rule--left"></div>
    <div class="double-rule double-rule--right"></div>

    <div class="message">
      <p>Hello!</p>
      <p><span>My name is Dan Harlow &amp; I have extensive experience working on all</span>
      <span>types of residential &amp; commercial projects. I understand what it takes to</span>
      <span>pull all the people &amp; components together for a highly successful project.</span>
      <span>I work with top-notch engineers &amp; contractors to create buildings &amp;</span>
      <span>homes that will stand the test of time.</span></p>
      <p><span>I know the hard work that goes into any building project. There are</span>
      <span>environmental impact studies, structural issues, engineering challenges,</span>
      <span>code compliance snags &amp; many others. And I can work with any budget.</span></p>
      <p><span>My services can easily be tailored to meet your needs &amp; they’re designed</span>
      <span>to enhance every phase of the building process. I would love to speak to</span>
      <span>you about your next project.</span></p>
      <p>Please contact me. Thanks!</p>
    </div>

    <div class="contact">
      <span class="line"></span>
      <span>555.410.2286 &nbsp;|&nbsp; 555 Street Ave. City, State Zipcode</span>
      <span class="line"></span>
    </div>

    <div class="divider"></div>
    <div class="stamp-box"></div>
    <div class="address-line" style="top:277px"></div>
    <div class="address-line" style="top:333px"></div>
    <div class="address-line" style="top:390px"></div>
    <div class="address-line" style="top:446px"></div>
  </section>
</body>
</html>
```